Construction Company

Design a clutter free business card, it can be double-sided utilizing the logo for BDN Ltd simple with all relevant contact information.

Please also a letterhead design to function for the purposes of invoicing, all mail requirements, with header to be distinctive while the footer ties page together and incorporates all necessary information.

For now, please use generic / dummy text and when a winner is selected, I will disclose the contact information.

Hi Designers! Please read the updated brief which includes the design of a business card and letterhead. Thank you!

```html
<!DOCTYPE html>
<html lang="en">
<head>
<meta charset="utf-8">
<title>BDN Ltd — Business Card</title>
<link href="https://fonts.googleapis.com/css2?family=Lato:wght@400;700&family=Tinos:wght@700&family=Playfair+Display:wght@600&display=swap" rel="stylesheet">
<style>
  :root {
    --navy: #263d8a;
    --gold: #b38f2a;
    --white: #ffffff;
    --backdrop: #3a3b3d;
    --serif: "Tinos", "Times New Roman", serif;
    --sans: "Lato", Arial, sans-serif;
    --brand: "Playfair Display", Georgia, serif;
  }
  * { box-sizing: border-box; margin: 0; padding: 0; }
  html, body { width: 1200px; height: 1000px; overflow: hidden; }
  body {
    background: var(--backdrop);
    display: flex; flex-direction: column; align-items: center; justify-content: center;
    gap: 40px;
  }
  .card {
    width: 760px; height: 436px; border-radius: 30px; position: relative; overflow: hidden;
  }
  /* Front */
  .card--front { background: var(--navy); }
  .card--front .frame {
    position: absolute; inset: 24px; border: 2px solid var(--gold); border-radius: 14px;
  }
  .card--front .brand {
    position: absolute; inset: 0; display: flex; align-items: center; justify-content: center; gap: 18px;
  }
  .brand-dot { width: 22px; height: 22px; border-radius: 50%; background: var(--gold); }
  .brand-name {
    font-family: var(--brand); font-weight: 600; font-size: 84px; letter-spacing: 2px; color: var(--white);
  }
  /* Back */
  .card--back { background: var(--white); }
  .card--back .address-band {
    position: absolute; left: 0; right: 0; bottom: 0; height: 74px; background: var(--navy);
    display: flex; align-items: center; justify-content: center;
    font-family: var(--serif); font-weight: 700; font-size: 21px; letter-spacing: .5px; color: var(--white);
  }
  .card--back .brand {
    position: absolute; left: 60px; top: 120px; width: 300px; height: 130px;
    display: flex; align-items: center; gap: 14px;
  }
  .card--back .brand-name { color: var(--navy); font-size: 60px; }
  .card--back .brand-dot { width: 18px; height: 18px; }
  .divider {
    position: absolute; left: 398px; top: 60px; width: 2px; height: 240px; background: var(--navy);
  }
  .details { position: absolute; left: 428px; top: 62px; }
  .person-name {
    font-family: var(--sans); font-weight: 700; font-size: 32px; letter-spacing: 3px; color: var(--gold);
  }
  .person-role { font-family: var(--sans); font-size: 21px; color: var(--navy); margin-top: 2px; }
  .contact-list { list-style: none; margin-top: 22px; display: flex; flex-direction: column; gap: 14px; }
  .contact-list li {
    display: flex; align-items: center; gap: 12px;
    font-family: var(--serif); font-weight: 700; font-size: 21px; color: var(--navy); letter-spacing: .5px;
  }
  .contact-list svg { width: 24px; height: 24px; flex: none; }
  .accent { color: var(--gold); }
</style>
</head>
<body>
  <section class="card card--front" aria-label="Card front">
    <div class="frame"></div>
    <div class="brand">
      <span class="brand-dot"></span>
      <span class="brand-name">BDN Ltd</span>
    </div>
  </section>

  <section class="card card--back" aria-label="Card back">
    <div class="brand">
      <span class="brand-dot"></span>
      <span class="brand-name">BDN Ltd</span>
    </div>
    <div class="divider"></div>
    <div class="details">
      <h1 class="person-name">YOUR DESIGN</h1>
      <p class="person-role">Managing Director</p>
      <ul class="contact-list">
        <li>
          <svg viewBox="0 0 24 24" aria-hidden="true"><circle cx="12" cy="12" r="12" fill="#b38f2a"/><path d="M7 9c0-1 1-2 2-2l1.5 2.5-1 1c.6 1.5 1.5 2.4 3 3l1-1L16 14c0 1-1 2-2 2-4 0-7-3-7-7z" fill="#263d8a"/></svg>
          <span>012 3456 789</span>
        </li>
        <li>
          <svg viewBox="0 0 24 24" aria-hidden="true"><circle cx="12" cy="12" r="12" fill="#b38f2a"/><rect x="6" y="8" width="12" height="8" fill="#263d8a"/><path d="M6 8l6 5 6-5" fill="none" stroke="#b38f2a" stroke-width="1.2"/></svg>
          <span>info@bdnltd.com</span>
        </li>
        <li>
          <svg viewBox="0 0 24 24" aria-hidden="true"><circle cx="12" cy="12" r="12" fill="#b38f2a"/><circle cx="12" cy="12" r="6" fill="none" stroke="#263d8a" stroke-width="1.5"/><ellipse cx="12" cy="12" rx="2.5" ry="6" fill="none" stroke="#263d8a" stroke-width="1.2"/><path d="M6 12h12" stroke="#263d8a" stroke-width="1.2"/></svg>
          <span>www.<span class="accent">bdnltd</span>.com</span>
        </li>
      </ul>
    </div>
    <footer class="address-band">01, BDNltd building, Your Street, Your Country Code - 12345</footer>
  </section>
</body>
</html>
```